Design Card that Captures Life's Moments

Thinking black and white design with maybe some accent colors. Open to others too. Looking for bold and modern to accompany new logo design. For the side without my info, would have tagline of "Capturing Life's Moments" with either logo or website tessabrimphotography.com. I want the tagline to dominate and be the main focus of that side.

Target Market(s)

Something that can appeal to people who might be interested in family/kids, business, sports, commercial, or birth/newborn photography.

Industry/Entity Type

Professional Photography

Contact Information for Business Card

Font styles to use
Sans Serif
Script
Other font styles liked:
• Go with Logo, but the tagline could be script that popped.

Requirements
Must have
• See details above! Wow factor! Make someone pick my card up and take it home or at least to look at it further.
• Tagline: Capturing Life's Moments (Main text on side without name)
• INFO:
• Tessa Brimford-Kole - Photographer
• 555-213-0476 - Cell and for SMS
• www.tessabrimphotography.com - Website (maybe on side with tagline?)
• tessa@tessaphotographs.com - Email
Nice to have
• JUST AN IDEA... I would like to see Capturing Life's Moment really take over most of one side of the card. Think greeting card. Where you can't miss it. It is in your face, but nice and elegant. Maybe cursive, but could work with other font. Instead of logo on tagline side, just have tessabrimphotography.com in smaller text along one of the edges.
Should not have
• Too simple I could of created it, like with only my logo and some typed text.

```html
<!DOCTYPE html>
<html lang="en">
<head>
<meta charset="utf-8">
<title>Tessa Brimford-Kole Photography – Business Card</title>
<link href="https://fonts.googleapis.com/css2?family=Open+Sans:wght@400;600;700&display=swap" rel="stylesheet">
<style>
  :root {
    --canvas: #ecebe8;
    --card: #ffffff;
    --ink: #1f1f1f;
    --band: #2b2b2d;
    --band-text: #ffffff;
    --mark-grey: #d2d2d2;
    --rail-grey: #a8a8a8;
  }
  * { box-sizing: border-box; margin: 0; padding: 0; }
  html, body { width: 1200px; height: 675px; overflow: hidden; }
  body {
    background: var(--canvas);
    font-family: "Open Sans", Arial, sans-serif;
    color: var(--ink);
    position: relative;
  }
  .card {
    position: absolute;
    top: 189px;
    width: 520px;
    height: 297px;
    background: var(--card);
    box-shadow: 0 6px 18px rgba(0,0,0,0.18);
    overflow: hidden;
  }
  .card--front { left: 55px; }
  .card--back { left: 625px; }

  /* Front */
  .frame-line {
    position: absolute;
    top: 0;
    width: 1.5px;
    background: var(--ink);
  }
  .frame-line--left { left: 100px; height: 240px; }
  .frame-line--right { left: 418px; height: 182px; }
  .camera-mark {
    position: absolute;
    left: 195px;
    top: 50px;
    width: 128px;
    height: 102px;
    display: block;
  }
  .tagline {
    position: absolute;
    left: 110px;
    top: 208px;
    white-space: nowrap;
    font-weight: 700;
    font-size: 20.5px;
    line-height: 1.2;
    letter-spacing: -0.1px;
    color: var(--ink);
  }
  .web-band {
    position: absolute;
    left: 0; right: 0; bottom: 0;
    height: 46px;
    background: var(--band);
    display: flex;
    align-items: center;
    justify-content: flex-end;
    padding-right: 70px;
  }
  .web-band__url {
    color: var(--band-text);
    font-size: 14px;
    letter-spacing: 0.4px;
    white-space: nowrap;
  }

  /* Back */
  .brand-name {
    position: absolute;
    left: 20px;
    top: 152px;
    width: 208px;
    text-align: right;
    font-size: 19px;
    font-weight: 400;
    white-space: nowrap;
    color: var(--ink);
  }
  .info-rail {
    position: absolute;
    left: 246px;
    top: 95px;
    width: 22px;
    height: 113px;
    background: var(--rail-grey);
  }
  .info-rail__icon {
    position: absolute;
    left: 4px;
    width: 14px;
    height: 14px;
  }
  .person {
    position: absolute;
    left: 283px;
    top: 88px;
    white-space: nowrap;
  }
  .person__name {
    font-size: 22px;
    font-weight: 400;
    line-height: 1.25;
  }
  .person__role {
    font-size: 15px;
    line-height: 1.35;
  }
  .contact-list {
    position: absolute;
    left: 283px;
    top: 149px;
    list-style: none;
    font-size: 12.5px;
    line-height: 18.5px;
    white-space: nowrap;
  }
  .services-band {
    position: absolute;
    left: 0; right: 0; bottom: 0;
    height: 27px;
    background: var(--band);
    color: var(--band-text);
    font-size: 11.5px;
    display: flex;
    align-items: center;
    justify-content: center;
    letter-spacing: 0.1px;
    white-space: nowrap;
  }
</style>
</head>
<body>

<section class="card card--front" aria-label="Card front">
  <div class="frame-line frame-line--left"></div>
  <div class="frame-line frame-line--right"></div>
  <svg class="camera-mark" viewBox="0 0 128 102" role="img" aria-label="Camera symbol of the photography brand">
    <rect x="0" y="0" width="128" height="102" rx="8" fill="var(--mark-grey)"/>
  </svg>
  <h1 class="tagline">Capturing Life's Moments</h1>
  <div class="web-band">
    <span class="web-band__url">www.tessabrimphotography.com</span>
  </div>
</section>

<section class="card card--back" aria-label="Card back">
  <div class="brand-name">Tessa Brimford</div>

  <div class="info-rail">
    <svg class="info-rail__icon" style="top:60px" viewBox="0 0 14 14" aria-hidden="true">
      <rect x="1" y="10" width="2" height="3" fill="#fff"/>
      <rect x="4" y="8" width="2" height="5" fill="#fff"/>
      <rect x="7" y="6" width="2" height="7" fill="#fff"/>
      <rect x="10" y="4" width="2" height="9" fill="#fff"/>
    </svg>
    <svg class="info-rail__icon" style="top:79px" viewBox="0 0 14 14" aria-hidden="true">
      <rect x="1" y="3" width="12" height="8.5" fill="none" stroke="#fff" stroke-width="1.2"/>
      <path d="M1 3 L7 8 L13 3" fill="none" stroke="#fff" stroke-width="1.2"/>
    </svg>
    <svg class="info-rail__icon" style="top:96px" viewBox="0 0 14 14" aria-hidden="true">
      <circle cx="7" cy="7" r="5.5" fill="none" stroke="#fff" stroke-width="1.2"/>
      <ellipse cx="7" cy="7" rx="2.3" ry="5.5" fill="none" stroke="#fff" stroke-width="1"/>
      <line x1="1.5" y1="7" x2="12.5" y2="7" stroke="#fff" stroke-width="1"/>
    </svg>
  </div>

  <div class="person">
    <h2 class="person__name">Tessa Brimford-Kole</h2>
    <p class="person__role">Photographer</p>
  </div>

  <ul class="contact-list">
    <li>555-213-0476</li>
    <li>tessa@tessaphotographs.com</li>
    <li>www.tessabrimphotography.com</li>
  </ul>

  <div class="services-band">Fashion | New Borns | Weddings | Products | Corporate | Portfolios</div>
</section>

</body>
</html>
```